Web Design Project for Industrial Hemp

I'm launching a new company to grow Industrial Hemp and then to set up a manufacturing facility to process the crop each and every year. We require a complete end to end brand and livery suite and we will start with a web presence. We want to appeal to (a) Investors, Employees, Farmers, and consumers so as to engage with all our stakeholders. We want to create a whole new industry that becomes a game changer for environmentally friendly crop production. Hemp is gaining in popularity and credibility across the world!

Target Market(s)

Farmers to produce, Manufacturers who will purchase the raw materials, Investors who will invest in the project, Consumers who will buy Hemp Products

Industry/Entity Type

Industry

Requirements
Must have
• Environmentally Friendly
Carbon Neutral/Positive
Game Changer
Multi-Use Crop
50,000 products can be made from Hemp
Should not have
• Should avoid its relationship with cannabis but not ignore it! When the regulatory bodies acknowledge the benefits of cannabanoids, they will start to legalise the production of cannabis for sale on prescription

```html
<!DOCTYPE html>
<html lang="en">
<head>
<meta charset="utf-8">
<title>Greenfield Hemp Co</title>
<link rel="stylesheet" href="https://fonts.googleapis.com/css2?family=Roboto:ital,wght@0,300;0,400;1,300;1,400&display=swap">
<style>
  :root {
    --page-bg: #2f5203;
    --white: #ffffff;
    --brand-green: #7dc21e;
    --brand-dark: #2f5203;
    --footer-green: #9bc05a;
    --text-grey: #666666;
    --buy-yellow: #fbc800;
    --black: #000000;
  }
  * { box-sizing: border-box; margin: 0; padding: 0; }
  html, body {
    width: 1088px; height: 1200px; overflow: hidden;
    background: var(--page-bg);
    font-family: "Roboto", "Helvetica Neue", Arial, sans-serif;
    font-weight: 300;
  }
  .site {
    position: absolute; left: 87px; top: 0; width: 907px; height: 1200px;
    background: var(--white);
  }
  .site-header { position: relative; height: 192px; }
  .brand {
    position: absolute; left: 20px; top: 76px;
    display: flex; align-items: center; gap: 10px;
    color: var(--brand-dark); font-size: 22px; font-weight: 400;
  }
  .brand-dot { width: 26px; height: 26px; border-radius: 50%; background: var(--brand-green); }
  .main-nav { position: absolute; top: 13px; left: 346px; height: 41px; }
  .main-nav a {
    position: absolute; top: 0; height: 41px; line-height: 41px;
    color: var(--brand-dark); text-decoration: none; font-size: 16px; font-weight: 400;
    white-space: nowrap;
  }
  .main-nav a.is-active { background: var(--brand-green); color: var(--white); padding: 0 18px; }
  .band { height: 11px; background: var(--brand-green); }
  .hero { position: relative; height: 363px; overflow: hidden; }
  .hero-photo {
    position: absolute; inset: 0;
    background: radial-gradient(circle at 70% 40%, #6fa63a 0%, #4f8a2a 45%, #3b6e22 100%);
  }
  .hero-title {
    position: absolute; left: 0; top: 0; width: 506px; height: 80px;
    background: rgba(40, 70, 20, 0.55);
    color: var(--white); font-size: 36px; font-weight: 300;
    padding: 17px 0 0 26px; letter-spacing: 0.3px;
  }
  .hero-text {
    position: absolute; left: 26px; top: 103px; width: 440px;
    color: var(--white); font-size: 20px; line-height: 26px;
  }
  .btn {
    position: absolute; top: 216px; height: 40px; line-height: 40px; width: 112px;
    text-align: center; font-size: 17px; font-weight: 400; text-decoration: none;
  }
  .btn-read { left: 30px; background: var(--brand-green); color: var(--white); }
  .btn-buy { left: 158px; background: var(--buy-yellow); color: var(--black); }
  .features { position: relative; height: 328px; }
  .feature { position: absolute; top: 40px; width: 230px; }
  .feature h2 { color: var(--brand-dark); font-size: 27px; font-weight: 300; margin-bottom: 15px; white-space: nowrap; }
  .feature p { color: var(--text-grey); font-size: 15.5px; line-height: 19.5px; margin-bottom: 19px; }
  .site-footer { position: relative; height: 231px; background: var(--footer-green); }
  .footer-brand {
    position: absolute; left: 28px; top: 102px;
    display: flex; align-items: center; gap: 8px;
    color: var(--brand-dark); font-size: 18px; font-weight: 400;
  }
  .footer-brand .brand-dot { width: 22px; height: 22px; }
  .footer-links { position: absolute; top: 26px; list-style: none; }
  .footer-links li { font-size: 15.5px; line-height: 27px; font-style: italic; font-weight: 400; color: var(--brand-dark); }
  .footer-base { height: 64px; background: var(--black); }
</style>
</head>
<body>
<div class="site">
  <header class="site-header">
    <div class="brand"><span class="brand-dot"></span>Greenfield Hemp Co</div>
    <nav class="main-nav">
      <a class="is-active" href="#" style="left:0">HOME</a>
      <a href="#" style="left:108px">ABOUT US</a>
      <a href="#" style="left:226px">PRODUCTS</a>
      <a href="#" style="left:353px">INVEST</a>
      <a href="#" style="left:444px">CONTACT</a>
    </nav>
  </header>
  <div class="band"></div>
  <section class="hero">
    <div class="hero-photo" role="img" aria-label="Photograph of a dense field of green hemp plants"></div>
    <h1 class="hero-title">LOREM IPSUM DOLOR SIT</h1>
    <p class="hero-text">lorem ipsum dolor sit amet consectetur adipiscing elit amet un quid ipsum dolor et un faq sin quid amet dikir consectetur adipiscing elit.</p>
    <a class="btn btn-read" href="#">read more</a>
    <a class="btn btn-buy" href="#">buy now</a>
  </section>
  <div class="band"></div>
  <section class="features">
    <article class="feature" style="left:68px">
      <h2>lorem ipsum dolor</h2>
      <p>lorem ipsum dolor sit amet consectetur adipiscing elit amet un quid ipsum dolor et un faq sin quid amet dikir adipiscing elit.</p>
      <p>Sit amet consectetur adipiscing elit amet un quid ipsum dolor et un faq sin quid amet dikir elit.</p>
    </article>
    <article class="feature" style="left:340px">
      <h2>lorem ipsum dolor</h2>
      <p>lorem ipsum dolor sit amet consectetur adipiscing elit amet un quid ipsum dolor et un faq sin quid amet dikir adipiscing elit.</p>
      <p>Sit amet consectetur adipiscing elit amet un quid ipsum dolor et un faq sin quid amet dikir elit.</p>
    </article>
    <article class="feature" style="left:612px">
      <h2>lorem ipsum dolor</h2>
      <p>lorem ipsum dolor sit amet consectetur adipiscing elit amet un quid ipsum dolor et un faq sin quid amet dikir adipiscing elit.</p>
      <p>Sit amet consectetur adipiscing elit amet un quid ipsum dolor et un faq sin quid amet dikir elit.</p>
    </article>
  </section>
  <footer class="site-footer">
    <div class="footer-brand"><span class="brand-dot"></span>Greenfield Hemp Co</div>
    <ul class="footer-links" style="left:260px">
      <li>lorem ipsum dolor sit</li><li>Dolor amett</li><li>Consectetur adipiscing</li><li>Elit quid un faq</li><li>Ipsum lorem</li><li>Dolor sit amet elit</li>
    </ul>
    <ul class="footer-links" style="left:478px">
      <li>lorem ipsum dolor sit</li><li>Dolor amett</li><li>Consectetur adipiscing</li><li>Elit quid un faq</li><li>Ipsum lorem</li><li>Dolor sit amet elit</li>
    </ul>
    <ul class="footer-links" style="left:696px">
      <li>lorem ipsum dolor sit</li><li>Dolor amett</li><li>Consectetur adipiscing</li><li>Elit quid un faq</li><li>Ipsum lorem</li><li>Dolor sit amet elit</li>
    </ul>
  </footer>
  <div class="footer-base"></div>
</div>
</body>
</html>
```